Marco Vessi Landing page

I need a Landing page for a website Marco Vessi. This is for an upscale clothing store for Men and Womens clothing and other items. It has to be elegant and unique in design and style.

Target Market(s)

Men, Women, Young adults 18-60

Coding

Number of Pages Required

1 page

Font styles to use
Decorative

Colors

Designer to choose colors to be used in the design.

```html
<!DOCTYPE html>
<html lang="en">
<head>
<meta charset="utf-8">
<title>Marco Vessi — Menswear &amp; Womenswear</title>
<link href="https://fonts.googleapis.com/css2?family=Roboto:wght@300;400;500&display=swap" rel="stylesheet">
<style>
:root{
  --navy:#0a3a9a;
  --sky:#00b4f0;
  --cyan:#00c4f4;
  --footer:#00c8fb;
  --text:#555a60;
  --muted:#6b7078;
  --panel:#f2f3f5;
  --white:#ffffff;
  --rule:#7fd6ef;
  --legal:#1d5fa8;
}
*{margin:0;padding:0;box-sizing:border-box}
html,body{width:1200px;height:2524px;overflow:hidden;background:var(--white)}
body{position:relative;font-family:'Roboto',sans-serif;font-weight:300;color:var(--text)}
.abs{position:absolute}
.center{left:0;width:1200px;text-align:center}
.rule{position:absolute;left:239px;width:722px;height:1px;background:var(--rule)}

/* header */
.site-header{position:absolute;left:0;top:0;width:1200px;height:91px;background:#fafafa}
.brand{position:absolute;left:127px;top:22px;font-size:31px;font-weight:500;color:var(--navy);letter-spacing:-0.3px}
.nav a{position:absolute;top:31px;font-size:17px;color:#5a5f66;text-decoration:none}
.nav a.active{color:var(--navy)}

/* hero */
.hero{position:absolute;left:0;top:91px;width:1200px;height:517px;background:linear-gradient(110deg,#00b8f2 0%,#0a8ee0 45%,#0052c0 80%,#003a9a 100%)}
.hero h1{top:160px;font-size:33px;font-weight:300;color:var(--white)}
.hero .rule{top:213px;background:rgba(255,255,255,.45)}
.hero p{top:236px;left:200px;width:800px;font-size:9.8px;line-height:14.5px;color:rgba(255,255,255,.92);text-align:center}
.btn-ghost{position:absolute;left:514px;top:313px;width:172px;height:38px;border:1px solid rgba(255,255,255,.85);border-radius:19px;color:var(--white);font-size:16px;line-height:36px;text-align:center}

/* about */
.about h2{top:658px;font-size:33px;font-weight:300;color:var(--navy)}
.about .rule{top:708px}
.about p{top:727px;left:200px;width:800px;font-size:9.8px;line-height:14.6px;color:var(--muted);text-align:center}

/* features */
.features{position:absolute;left:0;top:867px;width:1200px;height:403px;background:var(--panel)}
.card{position:absolute;top:44px;width:297px;height:315px;background:var(--white);border:1px solid #e4e6ea;border-radius:4px;text-align:center}
.card svg{position:absolute;left:109px;top:30px}
.card h3{position:absolute;left:0;width:100%;top:127px;font-size:33px;font-weight:300;color:var(--navy)}
.card p{position:absolute;left:45px;width:207px;top:225px;top:226px;font-size:13.4px;line-height:19px;color:var(--text)}
.card p{top:226px}
.card .copy{position:absolute;left:40px;width:217px;top:226px}
.card .btn-outline{position:absolute;left:89px;top:251px;width:118px;height:34px;border:1px solid var(--rule);border-radius:17px;font-size:13.4px;line-height:32px;color:var(--sky)}

/* testimonials */
.testimonials{position:absolute;left:0;top:1270px;width:1200px;height:433px;background:linear-gradient(180deg,#3e4146,#35383d)}
.testimonials h2{top:100px;font-size:33px;font-weight:300;color:var(--white)}
.testimonials .rule{top:151px;background:rgba(0,196,244,.5)}
.avatar{position:absolute;left:576px;top:190px;width:48px;height:48px;border-radius:50%;border:2px solid var(--cyan);background:linear-gradient(135deg,#e3e7ea,#7f8891)}
.testimonials p{top:252px;left:210px;width:780px;font-size:15px;line-height:21px;color:#e6e8ea;text-align:center}
.testimonials .name{top:314px;font-size:18px;color:var(--cyan)}

/* works */
.works h2{top:1755px;font-size:33px;font-weight:300;color:var(--cyan)}
.works .rule{top:1805px}
.work{position:absolute;top:1843px;width:295px;height:175px}

/* signup */
.signup{position:absolute;left:0;top:2077px;width:1200px;height:311px;background:linear-gradient(100deg,#0a45b0 0%,#0a78d8 45%,#00b6f0 80%,#00c2f4 100%)}
.signup h2{top:82px;font-size:33px;font-weight:300;color:var(--white)}
.signup .rule{top:128px;background:rgba(255,255,255,.4)}
.field{position:absolute;top:183px;width:213px;height:45px;border:1px solid rgba(255,255,255,.85);border-radius:3px;padding-left:15px;font-size:13.4px;line-height:43px;color:rgba(255,255,255,.92)}
.btn-solid{position:absolute;left:859px;top:183px;width:213px;height:45px;background:var(--cyan);border-radius:3px;font-size:13px;font-weight:400;line-height:45px;color:var(--white);text-align:center}

/* footer */
.site-footer{position:absolute;left:0;top:2388px;width:1200px;height:136px;background:var(--footer)}
.site-footer .brand{top:50px}
.legal{position:absolute;left:305px;top:51px;font-size:13px;line-height:19px;color:var(--legal)}
.follow{position:absolute;left:943px;top:42px;font-size:12.5px;color:var(--legal)}
.social{position:absolute;left:943px;top:62px;display:flex;gap:5px}
.social span{width:29px;height:29px;border-radius:50%;background:var(--navy)}
</style>
</head>
<body>

<header class="site-header">
  <div class="brand">Marco Vessi</div>
  <nav class="nav">
    <a style="left:660px">Home</a>
    <a class="active" style="left:735px">About Us</a>
    <a style="left:832px">Price List</a>
    <a style="left:929px">Blog</a>
    <a style="left:989px">Contact Us</a>
  </nav>
</header>

<section class="hero" role="img" aria-label="Blue-tinted atelier desk scene with laptop, plant, notebook and coffee cup">
  <h1 class="abs center">Welcome to our Website</h1>
  <div class="rule"></div>
  <p class="abs">Tailored menswear and refined womenswear, cut from fine Italian wool, silk and linen. Each season we gather timeless pieces, leather goods and accessories for those who dress with quiet confidence. Discover the new collection in our boutique.</p>
  <div class="btn-ghost">Know More</div>
</section>

<section class="about">
  <h2 class="abs center">Some information of About us</h2>
  <div class="rule"></div>
  <p class="abs">Marco Vessi began as a small tailoring house and grew into a boutique for men and women who value craft over trend. Our buyers travel to mills and ateliers to select fabrics that age beautifully, and every suit, dress and coat is finished by hand. We offer personal fittings, alterations and styling advice so that each garment feels made for you. From evening wear to relaxed weekend pieces, our rails change with the seasons, while the standard never does.<br>Visit the boutique to explore shirts, knitwear, handbags, shoes and fine accessories, chosen for lasting elegance and wrapped with care.</p>
</section>

<section class="features">
  <div class="card" style="left:127px">
    <svg width="78" height="78" viewBox="0 0 78 78"><circle cx="39" cy="39" r="37" fill="none" stroke="#0a3a9a" stroke-width="2.5"/><path d="M27 46h24l-3-4v-9a9 9 0 0 0-18 0v9z" fill="none" stroke="#0a3a9a" stroke-width="3" stroke-linejoin="round"/><path d="M35 49a4 4 0 0 0 8 0" fill="none" stroke="#0a3a9a" stroke-width="3"/><line x1="39" y1="21" x2="39" y2="24" stroke="#0a3a9a" stroke-width="3"/></svg>
    <h3>Why us?</h3>
    <p style="top:182px;left:30px;width:236px">Fine Italian fabrics, hand finished seams and a cut made to last.</p>
    <div class="btn-outline">Read More...</div>
  </div>
  <div class="card" style="left:452px">
    <svg width="78" height="78" viewBox="0 0 78 78"><circle cx="39" cy="39" r="37" fill="none" stroke="#0a3a9a" stroke-width="2.5"/><path d="M27 46h24l-3-4v-9a9 9 0 0 0-18 0v9z" fill="none" stroke="#0a3a9a" stroke-width="3" stroke-linejoin="round"/><path d="M35 49a4 4 0 0 0 8 0" fill="none" stroke="#0a3a9a" stroke-width="3"/><line x1="39" y1="21" x2="39" y2="24" stroke="#0a3a9a" stroke-width="3"/></svg>
    <h3>Why us?</h3>
    <p style="top:182px;left:30px;width:236px">Private fittings, free alterations and styling by our own tailors.</p>
    <div class="btn-outline">Read More...</div>
  </div>
  <div class="card" style="left:776px">
    <svg width="78" height="78" viewBox="0 0 78 78"><circle cx="39" cy="39" r="37" fill="none" stroke="#0a3a9a" stroke-width="2.5"/><path d="M27 46h24l-3-4v-9a9 9 0 0 0-18 0v9z" fill="none" stroke="#0a3a9a" stroke-width="3" stroke-linejoin="round"/><path d="M35 49a4 4 0 0 0 8 0" fill="none" stroke="#0a3a9a" stroke-width="3"/><line x1="39" y1="21" x2="39" y2="24" stroke="#0a3a9a" stroke-width="3"/></svg>
    <h3>Why us?</h3>
    <p style="top:182px;left:30px;width:236px">Curated collections for men and women, renewed every season.</p>
    <div class="btn-outline">Read More...</div>
  </div>
</section>

<section class="testimonials" role="img" aria-label="Dark-tinted desk scene with laptop, plant and coffee cup">
  <h2 class="abs center">Client Testimonials</h2>
  <div class="rule"></div>
  <div class="avatar" role="img" aria-label="Client portrait"></div>
  <p class="abs">The fitting was unhurried and precise, and my suit now feels like a second skin. Every detail, from the lining to the buttons, shows real care. I return each season for the new collection.</p>
  <div class="abs center name">Luca Ferri</div>
</section>

<section class="works">
  <h2 class="abs center">Our some works</h2>
  <div class="rule"></div>
  <div class="work" style="left:127px;background:linear-gradient(135deg,#f3f3f3,#e6dccb 60%,#efefef)" role="img" aria-label="Flat lay with tablet, gold laptop, coffee and flowers"></div>
  <div class="work" style="left:453px;background:linear-gradient(160deg,#f2f2f2,#cfd1d4 55%,#5a5d62)" role="img" aria-label="Laptop on a white desk with camera lenses"></div>
  <div class="work" style="left:778px;background:linear-gradient(135deg,#c9ccce,#d9dbdc 50%,#b9bcbe)" role="img" aria-label="Laptop on grey desk with plant, notebook and coffee cup"></div>
</section>

<section class="signup" role="img" aria-label="Blue-tinted desk scene background">
  <h2 class="abs center">Sign Up for more information</h2>
  <div class="rule"></div>
  <div class="field" style="left:127px">User Name</div>
  <div class="field" style="left:371px">Email Address</div>
  <div class="field" style="left:615px">Password</div>
  <div class="btn-solid">SIGN UP NOW</div>
</section>

<footer class="site-footer">
  <div class="brand">Marco Vessi</div>
  <div class="legal">Copyrights © 2014 All Rights Reserved<br>Terms of Use / Privacy Policy</div>
  <div class="follow">Follow us on:</div>
  <div class="social">
    <span role="img" aria-label="Social network link"></span><span role="img" aria-label="Social network link"></span><span role="img" aria-label="Social network link"></span><span role="img" aria-label="Social network link"></span>
  </div>
</footer>

</body>
</html>
```